Box Truck Wrap

We need to create a design for our 26' box trucks. We want it to be very attention grabbing yet simple and we would like it to be modeled after our existing branding. The final deliverable needs to be 75DPI (Or more) at scale. The size of the wrap will be approximately 26' long and 8' tall. Colors are red white and blue. Please no stock images and we dpnt want any photos of people. Examples of other company trucks are included. We need one design for the side and also one for the back. Approx 7' x 8'

```html
<!DOCTYPE html>
<html lang="en">
<head>
<meta charset="utf-8">
<title>Summit Haulers – Box Truck Wrap</title>
<link rel="stylesheet" href="https://fonts.googleapis.com/css2?family=Montserrat:wght@700&family=Poppins:wght@600;700&display=swap">
<style>
  :root {
    --red: #ec1c24;
    --navy: #2b1f63;
    --white: #ffffff;
    --page: #ffffff;
  }
  * { margin: 0; padding: 0; box-sizing: border-box; }
  html, body {
    width: 1200px;
    height: 1129px;
    overflow: hidden;
    background: var(--page);
  }
  .canvas {
    position: relative;
    width: 1200px;
    height: 1129px;
  }
  .wrap-layout {
    position: absolute;
    left: 40px;
    top: 430px;
    width: 1120px;
    height: 270px;
    display: flex;
    gap: 4px;
    box-shadow: 0 2px 6px rgba(0,0,0,0.12);
  }
  .panel {
    position: relative;
    height: 100%;
    overflow: hidden;
  }
  .panel-back { width: 238px; }
  .panel-side { width: 878px; }
  .panel-art {
    position: absolute;
    inset: 0;
    width: 100%;
    height: 100%;
    display: block;
  }
  .brand-block {
    position: absolute;
    top: 0;
    width: 0;
    height: 100%;
  }
  .brand-block > * {
    position: absolute;
    left: 0;
    transform: translateX(-50%);
    white-space: nowrap;
    line-height: 1;
    text-align: center;
  }
  .brand-dot { border-radius: 50%; }
  .brand-name {
    font-family: "Montserrat", sans-serif;
    font-weight: 700;
  }
  .phone {
    font-family: "Poppins", sans-serif;
    font-weight: 700;
  }
  .website {
    font-family: "Poppins", sans-serif;
    font-weight: 700;
  }

  /* Back door panel */
  .panel-back .brand-block { left: 50%; }
  .panel-back .brand-dot { top: 50px; width: 78px; height: 78px; background: var(--white); }
  .panel-back .brand-name { color: var(--white); }
  .panel-back .name-main { top: 134px; font-size: 27px; letter-spacing: 0.06em; padding-left: 0.06em; }
  .panel-back .name-sub { top: 163px; font-size: 13px; letter-spacing: 0.45em; padding-left: 0.45em; }
  .panel-back .phone { color: var(--white); top: 196px; font-size: 19px; }
  .panel-back .website { color: var(--white); top: 222px; font-size: 7.5px; letter-spacing: 0.03em; }

  /* Side panel */
  .panel-side .brand-block { left: 45.4%; }
  .panel-side .brand-dot { top: 20px; width: 112px; height: 112px; background: var(--navy); }
  .panel-side .brand-name { color: var(--red); }
  .panel-side .name-main { top: 137px; font-size: 40px; letter-spacing: 0.07em; padding-left: 0.07em; }
  .panel-side .name-sub { top: 180px; font-size: 23px; letter-spacing: 0.5em; padding-left: 0.5em; }
  .panel-side .phone { color: var(--navy); top: 206px; font-size: 25px; }
  .panel-side .website { color: var(--red); top: 239px; font-size: 10px; letter-spacing: 0.42em; padding-left: 0.42em; }
</style>
</head>
<body>
<main class="canvas">
  <section class="wrap-layout" aria-label="Box truck wrap layout: back doors and side">

    <article class="panel panel-back" aria-label="Back doors">
      <svg class="panel-art" viewBox="0 0 380 432" preserveAspectRatio="none" aria-hidden="true">
        <defs>
          <linearGradient id="backFade" x1="0" y1="0" x2="1" y2="0">
            <stop offset="0" stop-color="#2b1f63"/>
            <stop offset="0.45" stop-color="#ec1c24"/>
            <stop offset="1" stop-color="#ec1c24"/>
          </linearGradient>
        </defs>
        <rect width="380" height="432" fill="url(#backFade)"/>
        <path d="M0 330 Q55 360 65 432 L0 432 Z" fill="#2b1f63"/>
        <path d="M380 250 Q350 360 315 432 L380 432 Z" fill="#2b1f63"/>
      </svg>
      <div class="brand-block">
        <div class="brand-dot"></div>
        <div class="brand-name name-main">SUMMIT</div>
        <div class="brand-name name-sub">HAULERS</div>
        <div class="phone">(555) 214 0387</div>
        <div class="website">SUMMITHAULERSATX.COM</div>
      </div>
    </article>

    <article class="panel panel-side" aria-label="Truck side">
      <svg class="panel-art" viewBox="0 0 1400 432" preserveAspectRatio="none" aria-hidden="true">
        <defs>
          <linearGradient id="sideTopFade" x1="0" y1="0" x2="1" y2="0">
            <stop offset="0" stop-color="#ec1c24"/>
            <stop offset="0.25" stop-color="#ec1c24"/>
            <stop offset="0.45" stop-color="#2b1f63"/>
          </linearGradient>
          <linearGradient id="sideBottomFade" x1="0" y1="0" x2="1" y2="0">
            <stop offset="0.5" stop-color="#2b1f63"/>
            <stop offset="0.8" stop-color="#ec1c24"/>
            <stop offset="1" stop-color="#ec1c24"/>
          </linearGradient>
        </defs>
        <rect width="1400" height="432" fill="url(#sideTopFade)"/>
        <path d="M700 432 Q1150 330 1400 140 L1400 432 Z" fill="url(#sideBottomFade)"/>
        <path d="M420 0 L540 0 Q170 110 55 432 L0 432 L0 320 Q160 70 420 0 Z" fill="#2b1f63"/>
        <path d="M540 0 L1350 0 Q1230 330 860 432 L55 432 Q170 110 540 0 Z" fill="#ffffff"/>
        <path d="M1350 0 L1400 0 L1400 130 Q1260 380 960 432 L860 432 Q1230 330 1350 0 Z" fill="#2b1f63"/>
      </svg>
      <div class="brand-block">
        <div class="brand-dot"></div>
        <div class="brand-name name-main">SUMMIT</div>
        <div class="brand-name name-sub">HAULERS</div>
        <div class="phone">(555) 214 0387</div>
        <div class="website">SUMMITHAULERSATX.COM</div>
      </div>
    </article>

  </section>
</main>
</body>
</html>
```